Velbrook Naturals - High Quality Organic Cleaning Product

A product label for a foaming hand soap. Company is called "Velbrook Naturals" and the tagline is "The Cleaner Cleaner". Maybe lighter blue background with red letters, but open to what looks good. Want it to be a simple, clean and sophisticated design that looks fresh and stands out. This product has high quality organic ingredients hence the ingredients are "velbrook naturals" than other toxic chemical cleaners. Attached is label specifications as well as an image for stock language for left and right side of label for reference. Parts can be omitted, added or mixed and matched as needed.
Went on vacation/holiday
Moms

```html
<!DOCTYPE html>
<html lang="en">
<head>
<meta charset="utf-8">
<title>Velbrook Naturals – Foaming Hand Soap Label</title>
<link href="https://fonts.googleapis.com/css2?family=Open+Sans:wght@500;600;700&display=swap" rel="stylesheet">
<style>
  :root {
    --page-bg: #f2f3f5;
    --band-light: #aec3ff;
    --band-mid: #7f98e6;
    --band-dark: #4d66c4;
    --panel: #f7f7f6;
    --ink: #4a6ccd;
    --ink-strong: #3f62c6;
  }
  html, body {
    margin: 0;
    padding: 0;
    width: 1200px;
    height: 1200px;
    overflow: hidden;
    background: var(--page-bg);
    font-family: "Open Sans", Arial, sans-serif;
  }
  .canvas {
    position: relative;
    width: 1200px;
    height: 1200px;
  }
  .label {
    position: absolute;
    left: 250px;
    top: 100px;
    width: 700px;
    height: 1000px;
    background: linear-gradient(135deg, var(--band-light) 0%, var(--band-mid) 45%, var(--band-dark) 100%);
  }
  .label-panel {
    position: absolute;
    left: 72px;
    top: 68px;
    right: 72px;
    bottom: 68px;
    background: var(--panel);
    border-radius: 16px;
    color: var(--ink);
    text-align: center;
  }
  .brand {
    position: absolute;
    left: 0;
    right: 0;
    top: 96px;
    font-weight: 600;
    color: var(--ink);
    line-height: 1;
  }
  .brand-name {
    display: block;
    font-size: 72px;
    letter-spacing: -1px;
  }
  .brand-sub {
    display: block;
    font-size: 40px;
    margin-top: 6px;
    letter-spacing: 0.5px;
  }
  .tagline {
    position: absolute;
    left: 0;
    right: 0;
    top: 300px;
    font-size: 26px;
    font-weight: 500;
    letter-spacing: 0.3px;
  }
  .product-name {
    position: absolute;
    left: 0;
    right: 0;
    top: 470px;
    margin: 0;
    font-size: 58px;
    font-weight: 700;
    line-height: 1.5;
    color: var(--ink-strong);
  }
  .net-volume {
    position: absolute;
    left: 0;
    right: 0;
    bottom: 60px;
    font-size: 18px;
    font-weight: 600;
  }
</style>
</head>
<body>
<div class="canvas">
  <section class="label">
    <div class="label-panel">
      <div class="brand">
        <span class="brand-name">velbrook</span>
        <span class="brand-sub">NATURALS</span>
      </div>
      <div class="tagline">NATURALLY FRESH CARE</div>
      <h1 class="product-name">FOAMING<br>HAND SOAP</h1>
      <div class="net-volume">12 FL OZ (355ML)</div>
    </div>
  </section>
</div>
</body>
</html>
```